Web design for sitter site

We will be launching a sitter site in the coming months that focuses on sitters for children. The name of this site will be KinWatch.com
We will need:
1. main page design
2. site logo designed
3. subpages as well for the look of people's profiles, and job listings, etc (see links below)
We only need the design, photos, font files, etc. We do not need this site coded (no html), a ps job is fine.
Some competing sites in the space include - tendhaven.com and mindly.com
http://www.example-guardia.com/images/profile1.jpg
http://brookvaleshelf.example/wp-content/uploads/2013/09/mindly-review.png
http://www.pinecrestuni.example/hr/photos/tend_haven2.jpg
Thanks for your interest!
Target Market(s)
Mothers of children, mainly women
Industry/Entity Type
Online
Look and feel

```html
<!DOCTYPE html>
<html lang="en">
<head>
<meta charset="utf-8">
<title>KinWatch.com – Caregivers</title>
<link rel="stylesheet" href="https://fonts.googleapis.com/css2?family=Arimo:ital,wght@0,400;0,700;1,400;1,700&family=Kalam:wght@400;700&display=swap">
<style>
:root{
  --sky:#1ba6ec;
  --sky-light:#5cc3f4;
  --nav-active:#3b8f75;
  --green:#2fc47a;
  --grey-btn:#a9acb3;
  --rule:#4a8fb8;
  --ink:#333;
  --muted:#777;
  --label:#1a8fd6;
  --white:#fff;
}
*{margin:0;padding:0;box-sizing:border-box}
html,body{width:712px;height:1200px;overflow:hidden;background:var(--white)}
body{position:relative;font-family:"Arimo",Arial,sans-serif;color:var(--ink)}

/* header */
.header-wave{position:absolute;left:0;top:0}
.brand{position:absolute;left:30px;top:38px;font-family:"Arimo",Arial,sans-serif;font-weight:700;font-size:34px;color:var(--white);line-height:1}
.main-nav{position:absolute;left:258px;top:0;display:flex;height:44px;align-items:center}
.main-nav a{font-family:"Kalam",cursive;font-size:12px;color:var(--white);text-decoration:none;padding:0 10px;height:44px;line-height:44px}
.main-nav a.active{background:var(--nav-active)}
.search-box{position:absolute;left:584px;top:27px;width:100px;height:20px;background:var(--white);font-size:8px;color:#aaa;padding:5px 6px}
.advanced-search{position:absolute;left:630px;top:51px;font-size:7px;font-weight:700;color:var(--white)}

/* page heading */
.page-title{position:absolute;left:32px;top:152px;font-family:"Kalam",cursive;font-weight:700;font-size:26px;color:var(--label)}
.page-title small{font-size:11px;font-weight:400;margin-left:6px}

/* sort bar */
.sort-label{position:absolute;left:36px;top:226px;font-size:11px;color:var(--label)}
.sort-options{position:absolute;left:106px;top:220px;display:flex;gap:4px}
.sort-options span{background:var(--grey-btn);color:var(--white);font-size:8px;font-weight:700;height:25px;line-height:25px;padding:0 4px}
.custom-sort{position:absolute;left:481px;top:218px;width:99px;height:29px;border:1px solid var(--green);font-size:8px;color:#999;text-align:center;line-height:27px}
.continue-btn{position:absolute;left:585px;top:218px;width:67px;height:29px;background:var(--green);color:var(--white);font-size:9px;font-weight:700;text-align:center;line-height:29px}

.rule{position:absolute;left:37px;width:616px;height:1px;background:var(--rule)}
.section-label{position:absolute;top:309px;font-size:11px;color:var(--label)}

/* caregiver cards */
.caregiver{position:absolute;left:0;width:712px;height:200px}
.caregiver .photo{position:absolute;left:35px;top:-5px;width:92px;height:124px}
.caregiver .name{position:absolute;left:140px;top:-6px;font-size:11px;color:var(--ink)}
.caregiver .meta{position:absolute;left:140px;top:9px;font-size:7.5px;font-weight:700;color:#555}
.caregiver .quote{position:absolute;left:140px;top:48px;width:160px;font-size:7.5px;font-weight:700;font-style:italic;color:var(--muted);line-height:1.3}
.caregiver .skills{position:absolute;left:140px;top:106px;font-size:7.5px;font-weight:700;color:#555;line-height:1.6}
.caregiver .skills span{color:var(--muted)}
.caregiver .terms{position:absolute;left:37px;top:124px;font-size:11px;color:var(--ink);line-height:1.35}
.caregiver .rate{position:absolute;left:37px;top:160px;font-size:13px;font-weight:700;color:#444}
.caregiver .btn{position:absolute;top:148px;height:27px;width:66px;color:var(--white);font-size:7.5px;font-weight:700;text-align:center;line-height:27px}
.caregiver .btn.profile{left:143px;background:var(--grey-btn)}
.caregiver .btn.hire{left:243px;background:var(--green);width:65px}
.testimonials{position:absolute;left:365px;top:0;width:220px}
.testimonial{height:63px;font-size:7.5px;font-style:italic;font-weight:700;color:var(--muted);line-height:1.3}
.testimonial cite{display:block;margin-left:150px;margin-top:4px;font-style:normal;color:#555;line-height:1.4}

/* show more + footer */
.show-more{position:absolute;left:36px;top:1049px;width:617px;height:27px;background:var(--green);color:var(--white);font-size:8px;font-weight:700;text-align:center;line-height:27px}
.copyright{position:absolute;left:34px;top:1123px;font-size:8px;font-weight:700;color:#1e6fb0}
.social{position:absolute;left:34px;top:1141px;display:flex;gap:4px}
.social span{width:25px;height:25px}
.legal{position:absolute;left:551px;top:1157px;font-size:8px;font-weight:700;color:#1e6fb0}
.footer-band{position:absolute;left:0;top:1181px;width:712px;height:19px;background:var(--sky)}
.footer-band::after{content:"";position:absolute;left:0;top:5px;width:712px;height:3px;background:var(--white)}
</style>
</head>
<body>

<svg class="header-wave" width="712" height="140" viewBox="0 0 712 140" aria-hidden="true">
  <path d="M0 0H712V128C640 104 560 96 470 112C380 128 300 96 200 108C120 118 60 130 0 128Z" fill="var(--sky-light)"/>
  <path d="M0 0H712V112C640 90 560 80 470 96C380 112 300 80 200 92C120 102 60 116 0 112Z" fill="var(--sky)"/>
</svg>
<div class="brand">KinWatch</div>
<nav class="main-nav">
  <a href="#">Home Care</a>
  <a href="#" class="active">Child Care</a>
  <a href="#">Pet Care</a>
  <a href="#">Senior Care</a>
</nav>
<div class="search-box">search</div>
<div class="advanced-search">Advance Search</div>

<h1 class="page-title">Caregivers<small>Find the right caregiver for your family</small></h1>

<div class="sort-label">Sort View:</div>
<div class="sort-options">
  <span>Pet Experience</span><span>Senior Experience</span><span>Cooking Experience</span><span>Baby Experience</span>
</div>
<div class="custom-sort">add custom sort</div>
<div class="continue-btn">CONTINUE</div>

<div class="rule" style="top:268px"></div>
<div class="section-label" style="left:36px">Basic Information:</div>
<div class="section-label" style="left:365px">Testimonials:</div>

<article class="caregiver" style="top:339px">
  <div class="photo" role="img" aria-label="Portrait photo of the caregiver" style="background:linear-gradient(160deg,#e8c66a,#8a4a38 55%,#3a2a2a)"></div>
  <div class="name">Clara M. Dunn</div>
  <div class="meta">28yrs. ,&nbsp; Arizona, USA</div>
  <div class="quote">" I love kids! Hire me and you'll have no worries ;)"</div>
  <div class="skills">Skills:<br><span>Basic Cooking, Cleaning, Etc.</span></div>
  <div class="terms">Part-time<br>5yrs of exp.</div>
  <div class="rate">$18 / hr</div>
  <div class="btn profile">See full profile</div>
  <div class="btn hire">HIRE ME</div>
  <div class="testimonials">
    <div class="testimonial">" My kids are so happy when she's around. I got nothing to worry about when she's here..."<cite>Grant Ellory,<br>New York, USA</cite></div>
    <div class="testimonial">" My kids are so happy when she's around. I got nothing to worry about when she's here..."<cite>Grant Ellory,<br>New York, USA</cite></div>
    <div class="testimonial">" My kids are so happy when she's around. I got nothing to worry about when she's here..."<cite>Grant Ellory,<br>New York, USA</cite></div>
  </div>
</article>
<div class="rule" style="top:548px"></div>

<article class="caregiver" style="top:569px">
  <div class="photo" role="img" aria-label="Outdoor portrait photo of the caregiver" style="top:-2px;height:90px;background:linear-gradient(170deg,#7fb2d8,#c9a57d 55%,#4f7a44)"></div>
  <div class="name" style="top:6px">Rena T. Holm</div>
  <div class="meta" style="top:21px">28yrs. ,&nbsp; Arizona, USA</div>
  <div class="quote" style="top:53px">" I love kids! Hire me and you'll have no worries ;)"</div>
  <div class="skills" style="top:112px">Skills:<br><span>Basic Cooking, Cleaning, Etc.</span></div>
  <div class="terms" style="top:132px">Part-time<br>5yrs of exp.</div>
  <div class="rate" style="top:171px">$18 / hr</div>
  <div class="btn profile" style="top:163px">See full profile</div>
  <div class="btn hire" style="top:163px">HIRE ME</div>
  <div class="testimonials">
    <div class="testimonial">" My kids are so happy when she's around. I got nothing to worry about when she's here..."<cite>Grant Ellory,<br>New York, USA</cite></div>
    <div class="testimonial">" My kids are so happy when she's around. I got nothing to worry about when she's here..."<cite>Grant Ellory,<br>New York, USA</cite></div>
    <div class="testimonial">" My kids are so happy when she's around. I got nothing to worry about when she's here..."<cite>Grant Ellory,<br>New York, USA</cite></div>
  </div>
</article>
<div class="rule" style="top:785px"></div>

<article class="caregiver" style="top:816px">
  <div class="photo" role="img" aria-label="Full-length photo of the caregiver by a wall" style="top:-10px;height:119px;background:linear-gradient(175deg,#9fb0b8,#6a7c86 50%,#3e4a52)"></div>
  <div class="name">Marisol</div>
  <div class="meta">20yrs. ,&nbsp; New York, USA</div>
  <div class="quote" style="top:50px;width:232px">"My experience with caring for children started when I was very young. My mom wanted to stay at home when she had her kids so she decided..."</div>
  <div class="skills" style="top:109px">Skills:<br><span>Basic Cooking, Cleaning, Etc.</span></div>
  <div class="terms" style="top:132px">Part-time<br>5yrs of exp.</div>
  <div class="rate" style="top:168px">$18 / hr</div>
  <div class="btn profile" style="top:153px">See full profile</div>
  <div class="btn hire" style="top:153px">HIRE ME</div>
  <div class="testimonials">
    <div class="testimonial">" My kids are so happy when she's around. I got nothing to worry about when she's here..."<cite>Grant Ellory,<br>New York, USA</cite></div>
    <div class="testimonial">" My kids are so happy when she's around. I got nothing to worry about when she's here..."<cite>Grant Ellory,<br>New York, USA</cite></div>
    <div class="testimonial">" My kids are so happy when she's around. I got nothing to worry about when she's here..."<cite>Grant Ellory,<br>New York, USA</cite></div>
  </div>
</article>
<div class="rule" style="top:1031px"></div>

<div class="show-more">Show More</div>

<footer>
  <div class="copyright">(c) copyright 2014 KinWatch.com</div>
  <div class="social" aria-label="Social links">
    <span style="background:#3b5b98"></span>
    <span style="background:#3ea0dc"></span>
    <span style="background:#d34836"></span>
    <span style="background:#c4302b"></span>
  </div>
  <div class="legal">Terms | Policy | Careers</div>
  <div class="footer-band"></div>
</footer>

</body>
</html>
```